Professional & attention grabbing.

A business card design, front and back. I already have a logo I will attach, but I am open to something new as well.
Things to include:
Name:
Title:
Phone:
Email:
Wanting something that is professional but attention grabbing.
Also we do a lot of work using drones on natural gas pipelines (leading the future)if you want to include any of that. I'm open to ideas.
Target Market(s)
Natural gas transmission industry / greenhouse gas mitigation industry
Industry/Entity Type
Business
Contact Information for Business Card
All details have been conveyed above.
Colors
Designer to choose colors to be used in the design.
Look and feel
Each slider illustrates characteristics of the customer's brand and the style your logo design should communicate.

```html
<!DOCTYPE html>
<html lang="en">
<head>
<meta charset="utf-8">
<title>Kestrel Line Inspections – Business Card</title>
<link href="https://fonts.googleapis.com/css2?family=Open+Sans:wght@400;600;700&display=swap" rel="stylesheet">
<style>
  :root {
    --bg: #e9e7e3;
    --card: #ffffff;
    --ink: #3a3a3c;
    --charcoal: #3b3b3e;
    --red: #c4161c;
    --sky-top: #9fb8d6;
    --sky-low: #dfe5ec;
    --ground: #8a7f70;
    --ground-dark: #5e5447;
  }
  * { margin: 0; padding: 0; box-sizing: border-box; }
  html, body { width: 1200px; height: 900px; overflow: hidden; }
  body {
    background: var(--bg);
    font-family: "Open Sans", Arial, sans-serif;
    color: var(--ink);
    display: flex;
    align-items: center;
    justify-content: center;
    gap: 40px;
  }
  .card {
    position: relative;
    width: 540px;
    height: 309px;
    background: var(--card);
    overflow: hidden;
    box-shadow: 0 6px 18px rgba(0,0,0,0.18);
  }
  .card-back .site-photo {
    position: absolute;
    inset: 0;
    background: linear-gradient(180deg,
      var(--sky-top) 0%, var(--sky-low) 45%,
      #a59c8e 52%, var(--ground) 70%, var(--ground-dark) 100%);
  }
  .card-front .swoosh { position: absolute; inset: 0; width: 100%; height: 100%; }
  .identity { position: absolute; left: 30px; top: 40px; }
  .person-name { font-size: 20px; font-weight: 700; letter-spacing: 0.3px; line-height: 1.1; }
  .person-name .first { color: var(--red); }
  .person-name .last { color: var(--ink); }
  .person-title { font-size: 14px; font-weight: 400; margin-top: 3px; }
  .brand {
    position: absolute; right: 28px; top: 40px;
    display: flex; align-items: center; gap: 8px;
  }
  .brand-mark { width: 16px; height: 16px; background: var(--red); }
  .brand-name { font-size: 16px; font-weight: 700; color: var(--ink); }
  .contacts { position: absolute; left: 30px; top: 188px; list-style: none; }
  .contacts li { display: flex; align-items: center; gap: 8px; font-size: 14px; line-height: 22px; }
  .contacts svg { width: 12px; height: 12px; fill: var(--red); }
  .website {
    position: absolute; right: 24px; top: 240px;
    color: #ffffff; font-size: 12px; font-weight: 400;
    white-space: nowrap;
  }
</style>
</head>
<body>
  <section class="card card-back">
    <div class="site-photo" role="img" aria-label="Photo of a drone flying over a pipeline construction site with cranes and workers"></div>
  </section>

  <section class="card card-front">
    <svg class="swoosh" viewBox="0 0 540 309" preserveAspectRatio="none" aria-hidden="true">
      <path d="M0,309 L0,295 C180,293 320,250 540,140 L540,309 Z" fill="var(--charcoal)"/>
      <path d="M0,272 C120,272 260,248 380,196 C280,236 150,262 0,284 Z" fill="var(--red)"/>
    </svg>

    <div class="identity">
      <h1 class="person-name"><span class="first">DANIEL</span> <span class="last">HARPER</span></h1>
      <p class="person-title">Managing Director</p>
    </div>

    <div class="brand">
      <span class="brand-mark"></span>
      <span class="brand-name">Kestrel Line Inspections</span>
    </div>

    <ul class="contacts">
      <li>
        <svg viewBox="0 0 24 24" aria-hidden="true"><path d="M6.6 10.8a15 15 0 0 0 6.6 6.6l2.2-2.2a1 1 0 0 1 1-.25 11.4 11.4 0 0 0 3.6.57 1 1 0 0 1 1 1V20a1 1 0 0 1-1 1A17 17 0 0 1 3 4a1 1 0 0 1 1-1h3.5a1 1 0 0 1 1 1c0 1.25.2 2.45.57 3.57a1 1 0 0 1-.25 1z"/></svg>
        <span>(044)987654321</span>
      </li>
      <li>
        <svg viewBox="0 0 24 24" aria-hidden="true"><path d="M2 5h20v14H2z M2 5l10 8 10-8" /></svg>
        <span>hello@kestrelline.com</span>
      </li>
    </ul>

    <p class="website">www.kestrelline.com</p>
  </section>
</body>
</html>
```